Cover and label for Christian CD with lively original music for kids

The album title is Sun Over Hills. It's for children, but is also designed to be enjoyable for older members of the family to listen to. The final cover should reflect the over-arching theme of God's love from a Christian perspective. If it depicts children, It should be culturally and racially inclusive. It should evoke feelings of warmth, joy and belonging (or at least openness) for viewers. And it should appeal to kids and adults. There should be some bright color but no overwhelmingly "loud" designs please. Album title and artist name should be clear-Sun Over Hills and Miss Tilda respectively (may need flexibility on artist name as that has not been finalized). Label should be adapted from or complementary to cover art.

Industry/Entity Type

Christian

```html
<!DOCTYPE html>
<html lang="en">
<head>
<meta charset="utf-8">
<title>Sun Over Hills – Miss Tilda</title>
<link rel="stylesheet" href="https://fonts.googleapis.com/css2?family=Bodoni+Moda:ital,opsz,wght@1,6..96,700&family=Arimo&display=swap">
<style>
  :root {
    --page: #ffffff;
    --cover: #000000;
    --violet: #4a0d8a;
    --violet-soft: rgba(74, 13, 138, 0.85);
    --sky: #92d8f5;
    --sky-soft: rgba(146, 216, 245, 0.9);
    --azure: #0098d8;
    --azure-soft: rgba(0, 152, 216, 0.75);
    --ink-light: #ffffff;
  }
  html, body {
    margin: 0;
    padding: 0;
    width: 1200px;
    height: 1050px;
    overflow: hidden;
    background: var(--page);
  }
  .canvas {
    position: relative;
    width: 1200px;
    height: 1050px;
    background: var(--page);
  }
  .cover {
    position: absolute;
    left: 110px;
    top: 117px;
    width: 980px;
    height: 816px;
    background: var(--cover);
    overflow: hidden;
  }
  .album-title {
    position: absolute;
    left: 0;
    right: 0;
    top: 14px;
    margin: 0;
    text-align: center;
    font-family: "Bodoni Moda", "Didot", serif;
    font-style: italic;
    font-weight: 700;
    font-size: 98px;
    line-height: 1.1;
    color: var(--violet);
    letter-spacing: 1px;
    white-space: nowrap;
  }
  .burst-artwork {
    position: absolute;
    left: 40px;
    top: 131px;
    width: 893px;
    height: 622px;
    border-radius: 50%;
    background:
      radial-gradient(ellipse 10% 12% at 49% 46%, var(--violet) 0%, var(--violet) 60%, rgba(74, 13, 138, 0) 100%),
      radial-gradient(ellipse 55% 38% at 52% 30%, var(--sky-soft) 0%, rgba(146, 216, 245, 0.45) 55%, rgba(146, 216, 245, 0) 100%),
      radial-gradient(ellipse 45% 45% at 48% 72%, var(--azure-soft) 0%, rgba(0, 152, 216, 0.4) 55%, rgba(0, 152, 216, 0) 100%),
      radial-gradient(ellipse 50% 30% at 30% 35%, var(--violet-soft) 0%, rgba(74, 13, 138, 0) 100%);
  }
  .artist-credit {
    position: absolute;
    right: 26px;
    bottom: 14px;
    margin: 0;
    font-family: "Arimo", "Arial", sans-serif;
    color: var(--ink-light);
    font-size: 29px;
    line-height: 1;
  }
  .artist-credit .label {
    font-size: 33px;
  }
</style>
</head>
<body>
  <main class="canvas">
    <section class="cover">
      <h1 class="album-title">Sun Over Hills</h1>
      <div class="burst-artwork" role="img" aria-label="Joyful burst of violet, sky blue and azure petal shapes radiating from a small violet heart, a sign of God's love"></div>
      <p class="artist-credit"><span class="label">Artist:</span> Miss Tilda</p>
    </section>
  </main>
</body>
</html>
```